Shoes, Handbags and Accessories

The main business of the company are shoes and then handbags, jewellery and scarves to accessorize.

The design I am looking for is a "shabby chic" design, cursive font, perhaps with a vintage country feel to it.

Target Market(s)

Age group are more for the 25+, but more so 35+ ladies.

Industry/Entity Type

Business

Contact Information for Business Card

Lantern Row Boutique & Accessories
Marcia Pellbrook - P.O. Box 482, Yarrabin W.A. 6391
Ph: (08) 97213356 fax: (08) 97213374 Mobile: 0419382716
Email:lanternrow@quillnet.com.au
Web: www.lanternrowboutique.com.au
Like us on facebook (facebook logo)

Requirements
Must have
• As already described. A "faded" picture background is also another feature I like, but I don't want to create a cluttered look about the business card.
Nice to have
• Classy, stylish and comfortable shoes.

```html
<!DOCTYPE html>
<html lang="en">
<head>
<meta charset="utf-8">
<title>Lantern Row Boutique &amp; Accessories – Business Card</title>
<link rel="stylesheet" href="https://fonts.googleapis.com/css2?family=Dancing+Script:wght@400;500&display=swap">
<style>
  :root {
    --stage: #93aeac;
    --front-purple: #6a2a9c;
    --front-purple-deep: #5a2188;
    --back-lilac: #e8d6e8;
    --ink-plum: #4a1f63;
    --band-purple: #6a2a9c;
    --white: #ffffff;
    --shoe-shade: rgba(60, 20, 90, 0.55);
    --ornament-light: rgba(190, 160, 215, 0.55);
    --ornament-deep: #6a2a9c;
  }
  * { margin: 0; padding: 0; box-sizing: border-box; }
  html, body {
    width: 1200px; height: 1000px; overflow: hidden;
    background: var(--stage);
  }
  .canvas { position: relative; width: 1200px; height: 1000px; }
  .card {
    position: absolute; left: 256px; width: 641px; height: 331px;
    border-radius: 10px; overflow: hidden;
    font-family: "Dancing Script", cursive;
  }
  .card--front { top: 107px; background: var(--front-purple); color: var(--white); }
  .card--back { top: 528px; height: 330px; background: var(--back-lilac); color: var(--ink-plum); }

  .shoe-art {
    position: absolute; left: 10px; top: 120px; width: 260px; height: 205px;
    background: radial-gradient(ellipse at 45% 60%, var(--shoe-shade), rgba(60,20,90,0) 70%);
  }
  .ornament-art {
    position: absolute; border-radius: 40% 40% 45% 45%;
  }
  .card--front .ornament-art {
    left: 528px; top: 78px; width: 64px; height: 150px;
    background: radial-gradient(ellipse, var(--ornament-light), rgba(190,160,215,0) 72%);
  }
  .card--back .ornament-art {
    left: 492px; top: 62px; width: 104px; height: 195px;
    background: radial-gradient(ellipse, var(--ornament-deep) 20%, rgba(106,42,156,0.25) 62%, rgba(106,42,156,0) 75%);
  }

  .brand { position: absolute; left: 0; width: 520px; text-align: center; }
  .card--front .brand { left: 40px; top: 38px; }
  .card--back .brand { left: 40px; top: 26px; }
  .brand__name { font-size: 46px; line-height: 1; font-weight: 500; }
  .card--back .brand__name { font-size: 40px; }
  .brand__amp { font-size: 22px; line-height: 1; margin-top: 16px; }
  .card--back .brand__amp { font-size: 16px; margin-top: 2px; }
  .brand__owner { font-size: 30px; line-height: 1; margin-top: 30px; }
  .card--back .brand__owner { font-size: 22px; margin-top: 6px; }

  .contact {
    position: absolute; left: 31px; top: 158px;
    list-style: none; font-size: 19px; line-height: 23px;
  }
  .contact li:nth-child(n+3) { font-size: 16px; }

  .web-band { position: absolute; left: 0; bottom: 0; width: 641px; height: 27px; }
  .web-band__url {
    position: absolute; right: 72px; bottom: 4px;
    font-family: "Dancing Script", cursive; font-size: 17px; color: var(--white);
  }
</style>
</head>
<body>
<main class="canvas">

  <section class="card card--front" aria-label="Business card front">
    <div class="shoe-art" role="img" aria-label="Faint silhouette of a high-heeled shoe"></div>
    <div class="ornament-art" role="img" aria-label="Faint decorative scroll ornament"></div>
    <div class="brand">
      <p class="brand__name">Lantern Row Boutique</p>
      <p class="brand__amp">&amp;</p>
      <p class="brand__owner">Accessories Marcia Pellbrook</p>
    </div>
  </section>

  <section class="card card--back" aria-label="Business card back">
    <div class="ornament-art" role="img" aria-label="Purple decorative scroll ornament"></div>
    <div class="brand">
      <p class="brand__name">Lantern Row Boutique</p>
      <p class="brand__amp">&amp;</p>
      <p class="brand__owner">Accessories Marcia Pellbrook</p>
    </div>
    <ul class="contact">
      <li>P.O. Box 482, Yarrabin W.A. 6391</li>
      <li>Ph: (08) 97213356</li>
      <li>Mobile: 0419382716</li>
      <li>Fax: (08) 97213374</li>
      <li>Email: lanternrow@quillnet.com.au</li>
    </ul>
    <svg class="web-band" viewBox="0 0 641 27" aria-hidden="true">
      <polygon points="294,27 312,5 641,5 641,27" fill="var(--band-purple)"/>
    </svg>
    <span class="web-band__url">www.lanternrowboutique.com.au</span>
  </section>

</main>
</body>
</html>
```